Graphic of Teacher Agility Framework

I need a model designed for my teacher educator agility framework. The concepts are responsive to each other on Figure 12 on the attachment and the text explains it all.

This is meant to be a conceptual framework of how ones thinks between experience, and theory, and research.

The domains represent a hierarchy of knowledge of specific domains that have enabled my learning to develop in-depth. I chose the term ‘agility framework’ to emphasise the importance of a responsiveness to the context and of the ability to respond with urgency between the various components (The Quillmark, 2012). I present the agility framework in Figure 12. The concentric circles are inter-connected as they are inter-dependent aspects of developing personal empowerment. The applicability of each domain relies on my ability to be aware of the context and to build work with urgency.

My learning has been iterative throughout this research, so this framework is intended to be understood as iterative, with movement between the concentric circles at a cognitive and behavioural level when greater awareness is gained. At the heart of the main circle are the researcherly dispositions that have been essential to my research and professional roles as well as to my personal learning. I have used descriptive headings for these dispositions that I believe are helpful for understanding them. The first one, ‘value deep understanding’, is modelled on Vostrup (2019); whilst ‘cognitive flexibility’ is an inter-cultural competency from Brasko et al (2014). I have also added in ‘responsiveness’ and ‘sensory awareness’ which I believe are additional dispositions that have emerged in this study. Whilst conducting this research I have been responsive to the context, the participants, and the data, whilst gaining a greater awareness of my place within UAE society.

Target Market(s)

Academic, research

Requirements
Must have
• Attractive Visuals
Nice to have
• Connections between the concepts

```html
<!DOCTYPE html>
<html lang="en">
<head>
<meta charset="utf-8">
<title>Teacher Agility Framework</title>
<link rel="stylesheet" href="https://fonts.googleapis.com/css2?family=Bebas+Neue&family=Roboto:wght@400;500;700;900&display=swap">
<style>
  :root {
    --page: #b9b6c6;
    --paper: #ffffff;
    --navy: #0a0f8c;
    --mint: #4cf0a0;
    --mint-dark: #16c060;
    --mint-light: #7de8b8;
    --magenta: #e01fc4;
    --pink-ring: #dc87d2;
    --blue-light: #a9c2fb;
    --blue-mid: #6c8cf5;
    --blue-deep: #4a55ec;
    --cyan: #b5f6f9;
    --royal: #0b3fd0;
    --orange: #e3a10f;
    --orange-light: #f2cf7c;
    --orange-mid: #f0b640;
    --green-bubble: #19c36a;
    --crimson: #d80a5c;
    --white: #ffffff;
  }
  html, body {
    margin: 0;
    width: 1200px;
    height: 1200px;
    overflow: hidden;
    background: var(--page);
  }
  .framework-board { display: block; width: 1200px; height: 1200px; }
  .title { font-family: "Bebas Neue", "Oswald", sans-serif; font-size: 74px; fill: var(--white); letter-spacing: 1px; }
  .label { font-family: "Roboto", Arial, sans-serif; font-weight: 500; fill: var(--white); }
  .satellite-label { font-size: 15px; }
  .ring-label { font-family: "Roboto", Arial, sans-serif; font-weight: 500; fill: var(--white); font-size: 25px; letter-spacing: 1px; }
  .research-label { font-family: "Roboto", Arial, sans-serif; font-weight: 500; fill: var(--royal); font-size: 17px; letter-spacing: 0.5px; }
  .bubble-label { font-family: "Roboto", Arial, sans-serif; font-weight: 500; fill: var(--white); font-size: 15px; }
  .quad-label { font-family: "Roboto", Arial, sans-serif; font-weight: 700; fill: var(--white); font-size: 13px; }
  .quad-small { font-size: 9px; }
  .empower-label { font-family: "Roboto", Arial, sans-serif; font-weight: 700; fill: var(--white); font-size: 17px; }
  .dots { fill: none; stroke-width: 3; stroke-dasharray: 2 5; stroke-linecap: round; }
  .icon-line { fill: none; stroke: var(--white); stroke-width: 3; stroke-linecap: round; stroke-linejoin: round; }
</style>
</head>
<body>
<svg class="framework-board" viewBox="0 0 1300 1300" xmlns="http://www.w3.org/2000/svg">
  <defs>
    <linearGradient id="ring-blue" x1="0" y1="0" x2="0" y2="1">
      <stop offset="0" stop-color="var(--blue-light)"/>
      <stop offset="1" stop-color="var(--blue-deep)"/>
    </linearGradient>
    <path id="arc-context" d="M 390 715 A 225 225 0 0 1 800 590"/>
    <path id="arc-research" d="M 460 640 A 160 160 0 0 1 760 640"/>
    <path id="arc-intercultural" d="M 420 920 A 268 268 0 0 1 470 465"/>
    <path id="arc-relationships" d="M 420 830 A 225 225 0 0 0 660 935"/>
  </defs>

  <!-- page -->
  <rect class="paper" x="46" y="178" width="1211" height="934" fill="var(--paper)"/>
  <g class="header">
    <rect x="46" y="178" width="1211" height="97" fill="var(--navy)"/>
    <line x1="46" y1="222" x2="293" y2="222" stroke="var(--white)" stroke-width="3"/>
    <line x1="1012" y1="227" x2="1257" y2="227" stroke="var(--white)" stroke-width="3"/>
    <text class="title" x="652" y="252" text-anchor="middle">TEACHER AGILITY FRAMEWORK</text>
  </g>

  <!-- connectors -->
  <g class="connectors">
    <path class="dots" stroke="var(--mint)" d="M 430 412 L 480 440"/>
    <path class="dots" stroke="var(--mint)" d="M 360 482 L 395 505"/>
    <path class="dots" stroke="var(--mint)" d="M 300 580 L 340 593"/>
    <path class="dots" stroke="var(--magenta)" d="M 315 890 L 350 868"/>
    <path class="dots" stroke="var(--magenta)" d="M 395 975 L 425 948"/>
  </g>

  <!-- satellites -->
  <g class="satellite satellite-time">
    <circle cx="432" cy="362" r="53" fill="var(--mint)"/>
    <text class="label satellite-label" x="432" y="340" text-anchor="middle">TIME</text>
    <path class="icon-line" d="M420 350 h24 M420 392 h24 M423 352 q0 12 9 19 q9 -7 9 -19 M423 390 q0 -12 9 -19 q9 7 9 19"/>
  </g>
  <g class="satellite satellite-speed">
    <circle cx="325" cy="445" r="53" fill="var(--mint)"/>
    <text class="label satellite-label" x="325" y="423" text-anchor="middle">SPEED</text>
    <path d="M330 430 L314 460 L326 460 L320 486 L338 452 L326 452 Z" fill="var(--white)"/>
  </g>
  <g class="satellite satellite-urgency">
    <circle cx="253" cy="558" r="53" fill="var(--mint)"/>
    <text class="label satellite-label" x="253" y="541" text-anchor="middle">URGENCY</text>
    <path d="M240 584 q3 -6 3 -16 q0 -14 10 -16 q10 2 10 16 q0 10 3 16 Z" fill="var(--white)"/>
    <circle cx="253" cy="589" r="4" fill="var(--white)"/>
    <path class="icon-line" d="M234 560 q-2 -6 2 -12 M272 560 q2 -6 -2 -12"/>
  </g>
  <g class="satellite satellite-self">
    <circle cx="270" cy="915" r="53" fill="var(--magenta)"/>
    <text class="label satellite-label" x="270" y="886" text-anchor="middle">SELF</text>
    <text class="label satellite-label" x="270" y="903" text-anchor="middle">AWARENESS</text>
    <rect x="248" y="912" width="44" height="38" rx="10" fill="var(--pink-ring)" role="img" aria-label="Seated meditation figure"/>
  </g>
  <g class="satellite satellite-reflexivity">
    <circle cx="358" cy="1017" r="53" fill="var(--magenta)"/>
    <text class="label satellite-label" x="358" y="1006" text-anchor="middle">REFLEXIVITY</text>
    <circle cx="358" cy="1030" r="14" class="icon-line"/>
    <path class="icon-line" d="M358 1044 v12 M348 1058 h20"/>
  </g>

  <!-- right branch shapes -->
  <g class="branches">
    <path d="M 780 520 Q 850 520 870 470 L 900 560 Q 830 600 830 690 L 830 760 Q 830 840 900 870 L 870 960 Q 850 900 780 900 Z" fill="var(--blue-mid)"/>
    <circle cx="968" cy="447" r="123" fill="var(--blue-light)"/>
    <circle cx="968" cy="955" r="125" fill="var(--blue-deep)"/>
  </g>

  <!-- main rings -->
  <g class="main-rings">
    <circle cx="577" cy="712" r="293" fill="var(--pink-ring)"/>
    <circle cx="600" cy="712" r="248" fill="url(#ring-blue)"/>
    <circle cx="610" cy="710" r="180" fill="var(--cyan)"/>
    <text class="ring-label"><textPath href="#arc-context" startOffset="30%">CONTEXT</textPath></text>
    <text class="ring-label"><textPath href="#arc-intercultural" startOffset="4%">INTERCULTURAL COMPETENCE</textPath></text>
    <text class="ring-label"><textPath href="#arc-relationships" startOffset="10%">RELATIONSHIPS</textPath></text>
    <text class="research-label"><textPath href="#arc-research" startOffset="6%">CONSUMPTION OF RESEARCH</textPath></text>
    <path class="dots" stroke="var(--white)" d="M 635 508 Q 740 520 780 590"/>
    <path class="dots" stroke="var(--white)" d="M 660 912 Q 760 895 785 830"/>
    <path class="dots" stroke="var(--white)" d="M 800 575 L 855 522"/>
    <path d="M 855 520 l -14 2 l 10 10 Z M 795 578 l 14 -2 l -10 -10 Z" fill="var(--white)"/>
    <path class="dots" stroke="var(--white)" d="M 800 835 L 855 880"/>
    <path d="M 860 884 l -14 -1 l 8 -11 Z M 796 830 l 14 1 l -8 11 Z" fill="var(--white)"/>
  </g>

  <!-- dispositions -->
  <g class="dispositions">
    <path d="M 575 790 Q 575 710 645 705 Q 735 700 745 790 Q 750 845 690 845 L 600 845 Q 575 840 575 790 Z" fill="var(--green-bubble)"/>
    <circle cx="698" cy="820" r="35" fill="var(--cyan)" opacity="0.5"/>
    <circle cx="565" cy="670" r="62" fill="var(--royal)"/>
    <circle cx="680" cy="650" r="57" fill="var(--magenta)"/>
    <circle cx="712" cy="686" r="50" fill="var(--magenta)"/>
    <circle cx="505" cy="715" r="57" fill="var(--orange)"/>
    <circle cx="525" cy="765" r="50" fill="var(--orange)"/>
    <text class="bubble-label" x="564" y="646" text-anchor="middle">Sensory</text>
    <text class="bubble-label" x="564" y="663" text-anchor="middle">Awareness</text>
    <rect x="584" y="674" width="46" height="56" rx="12" fill="var(--blue-mid)" role="img" aria-label="Body outline with heart"/>
    <text class="bubble-label" x="682" y="644" text-anchor="middle">Value Deep</text>
    <text class="bubble-label" x="682" y="661" text-anchor="middle">Understanding</text>
    <rect x="684" y="670" width="50" height="48" rx="12" fill="var(--pink-ring)" role="img" aria-label="Head profile with network"/>
    <text class="bubble-label" x="512" y="721" text-anchor="middle">Responsiveness</text>
    <path class="icon-line" d="M 545 750 A 20 20 0 1 1 528 745" stroke-width="4"/>
    <path d="M 545 742 l 4 14 l -12 -4 Z" fill="var(--white)"/>
    <circle cx="658" cy="750" r="20" class="icon-line" stroke-width="2"/>
    <text class="bubble-label" x="645" y="800" text-anchor="middle">Cognitive Flexibility</text>
  </g>

  <!-- context quadrants -->
  <g class="context-wheel">
    <circle cx="968" cy="447" r="100" fill="var(--mint-light)"/>
    <path d="M968 447 L890 370 A110 110 0 0 1 1046 370 Z" fill="var(--mint-light)"/>
    <path d="M968 447 L1046 370 A110 110 0 0 1 1046 524 Z" fill="var(--mint)"/>
    <path d="M968 447 L1046 524 A110 110 0 0 1 890 524 Z" fill="var(--mint-dark)"/>
    <path d="M968 447 L890 524 A110 110 0 0 1 890 370 Z" fill="var(--mint-dark)"/>
    <circle cx="968" cy="447" r="34" fill="var(--white)"/>
    <path d="M968 423 L988 431 Q988 458 968 470 Q948 458 948 431 Z" fill="var(--mint-dark)"/>
    <path class="icon-line" d="M958 447 l7 7 l13 -14"/>
    <text class="quad-label" x="968" y="374" text-anchor="middle">EMPLOYMENT</text>
    <text class="quad-label" x="968" y="388" text-anchor="middle">CONTRACTS</text>
    <text class="quad-label" x="898" y="444" text-anchor="middle">EDUCATION</text>
    <text class="quad-label quad-small" x="898" y="457" text-anchor="middle">REGULATION</text>
    <text class="quad-label" x="1041" y="442" text-anchor="middle">CULTURAL</text>
    <text class="quad-label quad-small" x="1041" y="454" text-anchor="middle">DIFFERENCES</text>
    <text class="quad-label" x="966" y="512" text-anchor="middle">MACRO</text>
    <text class="quad-label" x="966" y="526" text-anchor="middle">ECONOMIC</text>
    <text class="quad-label" x="966" y="540" text-anchor="middle">FACTORS</text>
  </g>

  <!-- personal empowerment -->
  <g class="empowerment">
    <ellipse cx="977" cy="665" rx="103" ry="82" fill="var(--crimson)"/>
    <text class="empower-label" x="977" y="624" text-anchor="middle">PERSONAL</text>
    <text class="empower-label" x="977" y="645" text-anchor="middle">EMPOWERMENT</text>
    <rect x="935" y="660" width="80" height="78" rx="14" fill="#e4477f" role="img" aria-label="Figure on a step reaching for a star"/>
    <path d="M977 758 l16 14 h-32 Z" fill="var(--crimson)"/>
    <path d="M977 780 l16 14 h-32 Z" fill="#e4509a"/>
    <path d="M977 802 l16 14 h-32 Z" fill="#f1a3c4"/>
  </g>

  <!-- relationships quadrants -->
  <g class="relationships-wheel">
    <path d="M968 955 L890 878 A110 110 0 0 1 1046 878 Z" fill="var(--orange-light)"/>
    <path d="M968 955 L1046 878 A110 110 0 0 1 1046 1032 Z" fill="var(--orange-mid)"/>
    <path d="M968 955 L1046 1032 A110 110 0 0 1 890 1032 Z" fill="var(--orange)"/>
    <path d="M968 955 L890 1032 A110 110 0 0 1 890 878 Z" fill="#e58a0c"/>
    <circle cx="968" cy="955" r="30" fill="var(--white)"/>
    <path d="M968 933 v44 M946 955 h44" stroke="var(--orange)" stroke-width="3"/>
    <path d="M968 930 l-6 8 h12 Z M968 980 l-6 -8 h12 Z M943 955 l8 -6 v12 Z M993 955 l-8 -6 v12 Z" fill="var(--orange)"/>
    <path class="icon-line" d="M925 875 Q968 858 1011 875 M925 1040 Q968 1057 1011 1040 M885 915 Q868 955 885 995 M1051 915 Q1068 955 1051 995" stroke-width="3"/>
    <text class="quad-label" x="968" y="894" text-anchor="middle">AGENCY</text>
    <text class="quad-label" x="904" y="956" text-anchor="middle">TACIT</text>
    <text class="quad-label quad-small" x="904" y="966" text-anchor="middle">KNOWLEDGE</text>
    <text class="quad-label quad-small" x="1034" y="960" text-anchor="middle">TENSIONS</text>
    <text class="quad-label" x="968" y="1017" text-anchor="middle">PERSONAL</text>
    <text class="quad-label" x="968" y="1031" text-anchor="middle">GROWTH</text>
  </g>
</svg>
</body>
</html>
```